Business Card Design

I'm looking for a cool business card design that showcases what my company does... I am the owner and Brava is a play on my last name. The Brava Group is a privately held entity that specializes in media (Brava Media) and financial services (Brava Trading).

Brava Media focuses on the distribution and management of quality entertainment properties to all areas of the media world including broadcast, cable, digital, mobile and social media. Brava Media helps media and entertainment companies create and market great content and ensure that it reaches the widest audience possible.

Brava Media currently represents Ripple TV (www.rippletv-example.com), the fastest growing over the air broadcast network that focuses on programming that appeals to the African American audience. Brava Media also represents two new over the air broadcast networks launching in Summer 2014 - Harbor TV (www.harbortv-example.com) and Maple TV (www.mapletv-example.com).

Brava Media is an investor and business partner in SunDrift (www.sundrift-example.com) - a mobile social platform that empowers the user to choose how long your photos and videos live online.

Brava Media also represents KRN Enterprises (www.krnent-example.com), an independent producer that creates talent-driven and cost-effective programming around emerging talent and Clearbrook Content, a prolific producer of multimedia content including QXN's hit program - Velvet Hall.

Brava Trading manages a family office and focuses on building meaningful partnerships with all major financial institutions with a heavy concentration on IPO and secondary offerings.

Industry/Entity Type

Entertainment

Contact Information for Business Card

Martin Hale
12 Cobalt Lane
Roslyn New York 11492
O 516.555.0143
C 516.555.0178

```html
<!DOCTYPE html>
<html lang="en">
<head>
<meta charset="utf-8">
<title>The Brava Group — Business Card</title>
<link href="https://fonts.googleapis.com/css2?family=Exo+2:wght@400;500&display=swap" rel="stylesheet">
<style>
  :root {
    --page-bg: #e9e6e2;
    --card-white: #fbfbf9;
    --brand-orange: #dd8426;
    --band-grey: #77716b;
    --name-grey: #5f5a55;
    --text-light: #ffffff;
    --divider: rgba(255, 255, 255, 0.55);
  }
  * { margin: 0; padding: 0; box-sizing: border-box; }
  html, body {
    width: 1200px;
    height: 800px;
    overflow: hidden;
    background: var(--page-bg);
    font-family: "Exo 2", sans-serif;
  }
  .canvas {
    width: 1200px;
    height: 800px;
    display: flex;
    align-items: center;
    justify-content: center;
  }
  .business-card {
    position: relative;
    width: 1050px;
    height: 600px;
    background: var(--card-white);
    overflow: hidden;
    box-shadow: 0 10px 30px rgba(0, 0, 0, 0.18);
  }
  .card-swoosh {
    position: absolute;
    inset: 0;
    width: 100%;
    height: 100%;
  }
  .swoosh-band { fill: var(--band-grey); }
  .swoosh-field { fill: var(--brand-orange); }

  .company-name {
    position: absolute;
    top: 96px;
    left: 72px;
    font-size: 44px;
    font-weight: 500;
    color: var(--name-grey);
    letter-spacing: 0.5px;
    line-height: 1;
    white-space: nowrap;
  }

  .contact-area {
    position: absolute;
    left: 0;
    right: 0;
    bottom: 48px;
    display: flex;
    justify-content: center;
    align-items: stretch;
    color: var(--text-light);
    font-size: 25px;
    font-weight: 500;
    line-height: 1.45;
    letter-spacing: 0.6px;
  }
  .identity-block {
    text-align: right;
    padding-right: 26px;
    white-space: nowrap;
  }
  .identity-block .role-sep { padding: 0 10px; }
  .contact-divider {
    width: 2px;
    background: var(--divider);
  }
  .channels-block {
    padding-left: 26px;
    display: grid;
    grid-template-columns: auto auto;
    column-gap: 22px;
    white-space: nowrap;
  }
</style>
</head>
<body>
<main class="canvas">
  <article class="business-card">
    <svg class="card-swoosh" viewBox="0 0 1050 600" preserveAspectRatio="none" aria-hidden="true">
      <path class="swoosh-band" d="M0,392 Q640,380 1050,-20 L1050,600 L0,600 Z"/>
      <path class="swoosh-field" d="M0,408 Q650,398 1050,0 L1050,600 L0,600 Z"/>
    </svg>

    <header>
      <h1 class="company-name">The Brava Group</h1>
    </header>

    <section class="contact-area">
      <div class="identity-block">
        <p>Martin Hale<span class="role-sep">|</span>Principal</p>
        <p>12 Cobalt Lane Roslyn</p>
        <p>New York 11492</p>
      </div>
      <div class="contact-divider"></div>
      <div class="channels-block">
        <span>Office:</span><span>516.555.0143</span>
        <span>Cell:</span><span>516.555.0178</span>
        <span>Email:</span><span>mhale@thebravagroup-example.com</span>
      </div>
    </section>
  </article>
</main>
</body>
</html>
```